Wine Label Design for Marrick Estate

I need a front and back label for a new wine I am making. I am looking for a classic, elegant and serious wine label. I would like the label to be white with blue and black writing. The blue will be the distinction in the label. The color of blue will be unique and catch the eye. The font of the writing will be unique and could also serve as the brand image for Marrick Estate. The label can have a design but should be simple and distinct. I envision the paper quality of the label to textured, high quality and add to the overall image of the label.
The label will be timeless. The price of this wine will be $85.00 a bottle, and the label should match a higher priced wine. This wine is family owned and operated.
The writing on the front and back label will be:

FRONT Label-

Marrick Estate

Howell Mountain

Napa Valley

2022 Cabernet Sauvignon

Back Label-

Cellared and Bottled by Marrick Estate, Larkfield, CA 94999

GOVERNMENT WARNING: (1) According to the Surgeon General, women should not drink alcoholic beverages during pregnancy because of the risk of birth defects. (2) Consumption of alcoholic beverages impairs your ability to drive a car or operate machinery, and may cause health problems.

Alc. 14.5% by Vol.

750 ml

Contains Sulfites

```html
<!DOCTYPE html>
<html lang="en">
<head>
<meta charset="utf-8">
<title>Marrick Estate – Wine Labels</title>
<link rel="stylesheet" href="https://fonts.googleapis.com/css2?family=IM+Fell+English+SC&display=swap">
<style>
  :root {
    --page: #ffffff;
    --paper: #f1f1f0;
    --estate-blue: #3b54a6;
    --ink: #2d2620;
    --black: #111111;
    --shadow: rgba(0, 0, 0, 0.12);
  }
  * { margin: 0; padding: 0; box-sizing: border-box; }
  html, body {
    width: 1200px; height: 877px; overflow: hidden;
    background: var(--page);
  }
  body {
    position: relative;
    font-family: "IM Fell English SC", "Times New Roman", serif;
    color: var(--ink);
  }
  .label {
    position: absolute;
    top: 37px;
    width: 540px;
    height: 751px;
    background: var(--paper);
    box-shadow: 0 1px 6px var(--shadow);
    text-align: center;
  }
  .label--front { left: 32px; }
  .label--back { left: 630px; }

  .abs { position: absolute; left: 0; right: 0; line-height: 1; white-space: nowrap; font-weight: 400; }

  /* Front */
  .brand-name { top: 88px; font-size: 50px; color: var(--black); letter-spacing: 1px; }
  .region-map {
    position: absolute; left: 169px; top: 205px; width: 199px; height: 240px;
    background: linear-gradient(180deg, #4560b0, var(--estate-blue));
    border-radius: 4px;
  }
  .appellation { font-size: 40px; color: var(--estate-blue); letter-spacing: 0.5px; }
  .appellation--sub { top: 497px; }
  .appellation--main { top: 547px; }
  .vintage { top: 653px; font-size: 29.5px; color: var(--black); }

  /* Back */
  .bottler-intro { top: 58px; font-size: 29.5px; color: var(--ink); }
  .bottler-name { top: 96px; font-size: 37px; color: var(--estate-blue); }
  .bottler-address { top: 136px; font-size: 33px; color: var(--estate-blue); }

  .warning {
    position: absolute; left: 44px; top: 205px; width: 450px; height: 279px;
    border: 1.5px solid var(--estate-blue);
    text-align: left;
    font-size: 24px; line-height: 26.7px; color: var(--ink);
    white-space: nowrap;
  }
  .warning__title { position: absolute; left: 53px; top: 15px; font-size: 23px; line-height: 1; }
  .warning__list { position: absolute; left: 15px; top: 42px; list-style: none; }
  .warning__item { display: flex; }
  .warning__num { width: 39px; flex: none; font-size: 20px; }

  .abv { top: 555px; font-size: 42px; color: var(--ink); }
  .volume { top: 597px; font-size: 42px; color: var(--ink); }
  .sulfites {
    position: absolute; left: 146px; top: 671px; width: 246px; height: 34px;
    background: var(--estate-blue); color: #fff;
    font-size: 29px; line-height: 36px; text-align: center; white-space: nowrap;
  }
</style>
</head>
<body>
  <section class="label label--front">
    <h1 class="abs brand-name">Marrick Estate</h1>
    <div class="region-map" role="img" aria-label="Silhouette map of the Howell Mountain wine region"></div>
    <p class="abs appellation appellation--sub">Howell Mountain</p>
    <p class="abs appellation appellation--main">Napa Valley</p>
    <p class="abs vintage">2022 Cabernet Sauvignon</p>
  </section>

  <section class="label label--back">
    <p class="abs bottler-intro">Cellared &amp; Bottled by</p>
    <p class="abs bottler-name">Marrick Estate</p>
    <p class="abs bottler-address">Larkfield, CA 94999</p>

    <div class="warning">
      <p class="warning__title">GOVERNMENT WARNING:</p>
      <ol class="warning__list">
        <li class="warning__item"><span class="warning__num">(1)</span><span>According to the Surgeon General,<br>women should not drink alcoholic<br>beverages during pregnancy because<br>of the risk of birth defects.</span></li>
        <li class="warning__item"><span class="warning__num">(2)</span><span>Consumption of alcoholic beverages<br>impairs your ability to drive a car<br>or operate machinery, and may cause<br>health problems.</span></li>
      </ol>
    </div>

    <p class="abs abv">Alc. 14.5% by Vol.</p>
    <p class="abs volume">750 ml</p>
    <p class="sulfites">Contains Sulfites</p>
  </section>
</body>
</html>
```